Infographic: Captive Insurance for the Cannabis Industry

I need an infographic designed for the attached article. The resulting document will be used in B2B content marketing and education, so it must be professional and clean and not an exercise in art. Colors used should be those of my logo found in the signature: blue, yellow & white. Design is up to the expert's discretion. I expect there will be a few iterations. ALSO: The chosen designer can expect many more projects using the same overall design, so it behooves you to participate. Please follow these directions and ask questions if unclear.

Target Market(s)

Business Owners, CFO's, CPAs Consultants, Commercial Real Estate Professionals

Font styles to use
Sans Serif

Requirements
Must have
• Clean professional design (not too overboard) using only the colors specified (see logo in signature- white, blue & gold/yellow)
• Images provided
• Call to action with link provided
• Signature block- use your discretion
• Everything you need is on the document
Should not have
• Too much clutter, wrong colors

```html
<!DOCTYPE html>
<html lang="en">
<head>
<meta charset="utf-8">
<title>Captive Insurance for the Cannabis Industry</title>
<link href="https://fonts.googleapis.com/css2?family=Montserrat:wght@400;500;600;700&display=swap" rel="stylesheet">
<style>
  :root{
    --blue:#0b4aa0;
    --yellow:#fcd42e;
    --ink:#3a3a3a;
    --paper:#ffffff;
    --stage:#a9a9a9;
    --stripe:#f1f2f4;
  }
  *{box-sizing:border-box;margin:0;padding:0}
  html,body{width:1200px;height:800px;overflow:hidden;background:var(--stage);font-family:'Montserrat',sans-serif;color:var(--ink)}
  .page{position:absolute;top:157px;width:364px;height:471px;background:var(--paper);overflow:hidden;box-shadow:0 2px 6px rgba(0,0,0,.18)}
  .page--one{left:50px}.page--two{left:427px}.page--three{left:804px}
  .stripes{position:absolute;inset:0;width:100%;height:100%}
  .abs{position:absolute}
  .headline{font-family:'Montserrat',sans-serif;font-weight:700;letter-spacing:.2px;line-height:1.32}
  .body{font-size:5.2px;line-height:1.38}
  .body p{margin-bottom:2.5px}
  .photo{position:absolute}
  .sub{color:var(--blue);font-weight:600}
  .footer{position:absolute;left:0;bottom:0;width:364px;height:35px}
  .footer__band{position:absolute;left:0;top:0}
  .footer__ask{position:absolute;left:20px;top:3px;font-size:7px;font-weight:600;color:#222}
  .footer__mail{position:absolute;left:18px;top:13px;display:flex;align-items:center;gap:4px;font-size:12.5px;font-weight:600;color:var(--blue)}
  .brand{position:absolute;right:22px;top:12px;display:flex;align-items:center;gap:4px;font-size:9px;font-weight:600;letter-spacing:1.5px;color:var(--blue)}
  .brand__dot{width:7px;height:7px;background:var(--yellow)}
  .colhead{font-size:6.6px;font-weight:600;color:var(--blue);padding-bottom:2px;border-bottom:1px solid var(--yellow);display:inline-block;margin-bottom:4px}
  .tick-list{list-style:none;font-size:5.3px;line-height:1.35;color:#fff}
  .tick-list li::before{content:"• ";color:var(--yellow)}
  .who{list-style:none;font-size:11.5px;font-weight:500;color:var(--blue);line-height:1.22}
  .who li::before{content:"• ";color:var(--yellow);font-size:8px;vertical-align:middle}
</style>
</head>
<body>

<!-- Page one -->
<section class="page page--one">
  <svg class="stripes" viewBox="0 0 364 471" aria-hidden="true">
    <polygon points="300,180 364,120 364,200 330,230" fill="var(--stripe)"/>
    <polygon points="200,420 300,330 330,340 240,430" fill="var(--stripe)"/>
  </svg>
  <svg class="abs" style="left:0;top:0" width="364" height="74" viewBox="0 0 364 74" aria-hidden="true">
    <polygon points="225,0 364,0 364,59 210,59" fill="var(--yellow)"/>
    <polygon points="0,0 225,0 210,73 0,73" fill="var(--blue)"/>
  </svg>
  <h1 class="abs headline" style="left:17px;top:14px;width:192px;font-size:7.2px;color:#fff">CAPTIVE INSURANCE FOR THE CANNABIS INDUSTRY: A UNIQUELY POWERFUL APPROACH TO MANAGE MONEY AND PROTECT ASSETS IN AN INDUSTRY THAT ISN'T SUPPORTED BY THE US BANKING SYSTEM</h1>
  <p class="abs" style="left:228px;top:11px;width:128px;font-size:4.9px;line-height:1.32;color:#333">Cannabis is illegal under federal law, despite being legal to cultivate and sell medical marijuana in most states. The cannabis industry suffers from many gray areas because of the frequent conflicting treatments of the industry between state and federal laws.</p>
  <h2 class="abs sub" style="left:18px;top:80px;width:330px;font-size:9px;line-height:1.25">One of the many hurdles facing Cannabis companies today is obtaining adequate business insurance.</h2>
  <div class="abs body" style="left:18px;top:113px;width:330px">
    <p>Because marijuana continues to be illegal under federal law, many traditional insurance companies have withdrawn from the cannabis market, following Harrow Street Underwriters' decision to get out of the industry altogether in 2015. The remaining insurance companies in the cannabis space charge notably higher premiums than for traditional businesses in response to the uncertainty of federal laws.</p>
    <p>Additionally, cannabis companies can find it difficult to insure certain risks. For example, many cannabis companies have taken massive hits from the hurricanes of 2017 and the current California wildfires.</p>
    <p>Given all the challenges facing cannabis companies today, is there a possible solution? How do you manage money and protect assets in an industry which isn't fully supported by the US banking system?</p>
  </div>
  <div class="photo" role="img" aria-label="Close-up of a hand in a suit holding a yellow strip reading Are You Covered" style="left:17px;top:186px;width:329px;height:148px;background:linear-gradient(120deg,#2a2a2a 0%,#6d6d6d 40%,#e9d63a 55%,#f5e44a 70%,#3a3a3a 100%)"></div>
  <div class="abs" style="left:18px;top:344px;width:150px">
    <div class="colhead">Enter captive insurance.</div>
    <p class="body">The challenges described above have created a perfect storm for cannabis companies to consider captive insurance companies. Popularized in the 1950's, captive insurance is a great alternative when the traditional insurance market fails the insured by being too costly, leaving too many gaps in coverage, or is unavailable.</p>
  </div>
  <div class="abs" style="left:184px;top:350px;width:1px;height:62px;background:#c8c8c8"></div>
  <div class="abs" style="left:201px;top:344px;width:150px">
    <div class="colhead">What is a Captive Insurance Company?</div>
    <p class="body">A wholly owned subsidiary company that provides risk-mitigation services for its parent company, or group of related companies. It's a form of corporate self-insurance. The financial benefits must be weighed against the administrative costs, and the insurance policies are subject to the same compliance rules as all insurance companies.</p>
  </div>
  <footer class="footer">
    <svg class="footer__band" width="364" height="35" viewBox="0 0 364 35" aria-hidden="true"><polygon points="0,0 227,0 240,35 0,35" fill="var(--yellow)"/></svg>
    <div class="footer__ask">Not sure if Captive Insurance is for you?</div>
    <div class="footer__mail"><svg width="15" height="15" viewBox="0 0 15 15" aria-hidden="true"><circle cx="7.5" cy="7.5" r="6.8" fill="none" stroke="#222" stroke-width="1.2"/><rect x="3.8" y="4.8" width="7.4" height="5.4" fill="none" stroke="#222" stroke-width="1"/><polyline points="3.8,4.8 7.5,8 11.2,4.8" fill="none" stroke="#222" stroke-width="1"/></svg>info@northbeamcaptive.com</div>
    <div class="brand"><span class="brand__dot"></span>NORTHBEAM</div>
  </footer>
</section>

<!-- Page two -->
<section class="page page--two">
  <svg class="stripes" viewBox="0 0 364 471" aria-hidden="true">
    <polygon points="300,230 364,170 364,250 330,280" fill="var(--stripe)"/>
  </svg>
  <div class="abs" style="left:0;top:0;width:364px;height:84px;background:var(--blue)"></div>
  <h1 class="abs headline" style="left:22px;top:17px;width:320px;text-align:center;font-size:8.4px;color:#fff">GIVEN THE NATURE OF THE INDUSTRY AND THE CHALLENGES FACING IT AS DESCRIBED ABOVE, CAPTIVE INSURANCE IS AN IDEAL SOLUTION FOR THE CANNABIS INDUSTRY.</h1>
  <div class="photo" role="img" aria-label="Cannabis leaves resting on a spread of dollar bills" style="left:17px;top:65px;width:329px;height:149px;background:linear-gradient(135deg,#c9c46a 0%,#e7e2a0 35%,#b3b13d 60%,#efe6c2 100%)"></div>
  <div class="abs body" style="left:19px;top:224px;width:320px">
    <p style="margin-bottom:1px"><span class="sub">Some of the benefits of captive insurance regarding risk management:</span><br>Increased insurance coverage<br>Increased efficiency of coverage – completely customized to pay only for what is needed<br>Full claim control<br>Improved underwriting flexibility to react to changing markets<br>Access to the reinsurance market</p>
    <p style="margin-top:4px;margin-bottom:1px"><span class="sub">Reduced insurance costs:</span><br>Eliminate paying for overhead and marketing costs charged by big insurance companies<br>Provides negotiation leverage with traditional insurance companies<br>Creates potential awareness within an organization for more efficient<br>loss prevention practices</p>
    <p style="margin-top:4px"><span class="sub">Improved Cash Flow:</span><br>Retain insurance premium dollars within the business to use at the owner's discretion<br>Increase investment income<br>Potential tax benefits (280E)</p>
  </div>
  <div class="abs" style="left:158px;top:340px;width:206px;height:80px;background:var(--blue)"></div>
  <div class="abs" style="left:202px;top:344px;width:160px">
    <div style="font-size:7.2px;font-weight:600;color:var(--yellow);margin-bottom:2px">These include but are not limited to:</div>
    <ul class="tick-list">
      <li>Crop insurance</li><li>Property and business interruption insurance</li><li>Cyber attacks</li><li>Auto &amp; product liability</li><li>Worker's compensation</li><li>Worker's personal injury</li><li>Intellectual property</li><li>Legal defense</li><li>Employee theft</li>
    </ul>
  </div>
  <div class="abs" style="left:20px;top:354px;width:172px;height:54px;background:var(--yellow);padding:5px 10px">
    <p style="font-size:7.1px;font-weight:600;color:var(--blue);line-height:1.3">There are many examples of gaps not covered by traditional insurance companies that captive insurance can be customized to address for the cannabis industry.</p>
  </div>
  <footer class="footer">
    <svg class="footer__band" width="364" height="35" viewBox="0 0 364 35" aria-hidden="true"><polygon points="0,0 227,0 240,35 0,35" fill="var(--yellow)"/></svg>
    <div class="footer__ask">Not sure if Captive Insurance is for you?</div>
    <div class="footer__mail"><svg width="15" height="15" viewBox="0 0 15 15" aria-hidden="true"><circle cx="7.5" cy="7.5" r="6.8" fill="none" stroke="#222" stroke-width="1.2"/><rect x="3.8" y="4.8" width="7.4" height="5.4" fill="none" stroke="#222" stroke-width="1"/><polyline points="3.8,4.8 7.5,8 11.2,4.8" fill="none" stroke="#222" stroke-width="1"/></svg>info@northbeamcaptive.com</div>
    <div class="brand"><span class="brand__dot"></span>NORTHBEAM</div>
  </footer>
</section>

<!-- Page three -->
<section class="page page--three">
  <svg class="stripes" viewBox="0 0 364 471" aria-hidden="true">
    <polygon points="300,280 364,220 364,300 330,330" fill="var(--stripe)"/>
  </svg>
  <div class="abs" style="left:0;top:0;width:364px;height:100px;background:var(--yellow)"></div>
  <h1 class="abs headline" style="left:20px;top:17px;width:324px;text-align:center;font-size:10.2px;color:var(--blue);line-height:1.38">THE KEY POINT IS, AS MENTIONED PREVIOUSLY, IS THAT CAPTIVE INSURANCE BENEFITS FROM COMPLETE CUSTOMIZATION BY THE OWNER.</h1>
  <div class="photo" role="img" aria-label="Scientist in a white coat inspecting cannabis plants in a grow room" style="left:17px;top:73px;width:329px;height:193px;background:linear-gradient(90deg,#4f7a2a 0%,#a9c383 30%,#f2f2ee 50%,#9fbf75 75%,#3f6a22 100%)"></div>
  <div class="abs" style="left:23px;top:258px;width:317px;height:32px;background:var(--blue);color:#fff;text-align:center;font-size:9.4px;font-weight:500;line-height:1.3;padding-top:3px">Captive insurance is not only a potential option for growers,<br>but any business that <span style="color:var(--yellow)">"touches"</span> marijuana, including:</div>
  <ul class="abs who" style="left:22px;top:302px">
    <li>Cultivators</li><li>Distributors</li><li>Dispensaries</li><li>Doctors</li>
  </ul>
  <ul class="abs who" style="left:123px;top:302px">
    <li>Property owners</li><li>Events</li><li>Supplies</li>
  </ul>
  <p class="abs body" style="left:18px;top:368px;width:330px">Despite having made a case for the consideration of captive insurance by companies in the cannabis niche, this is not a slam dunk solution and challenges still exist because marijuana is still illegal under federal law. Additionally, creating the captive company can be very complex. Therefore, any captive must be developed in conjunction with a qualified captive manager who knows the qualified jurisdictions that can license a captive insurance company for the cannabis industry. The risk of a captive being prosecuted at the federal level is low, but still possible until the federal laws are updated. The captive must be structured to ensure that the business operates in accordance with the applicable state laws.</p>
  <footer class="footer">
    <svg class="footer__band" width="364" height="35" viewBox="0 0 364 35" aria-hidden="true"><polygon points="0,0 227,0 240,35 0,35" fill="var(--yellow)"/></svg>
    <div class="footer__ask">Not sure if Captive Insurance is for you?</div>
    <div class="footer__mail"><svg width="15" height="15" viewBox="0 0 15 15" aria-hidden="true"><circle cx="7.5" cy="7.5" r="6.8" fill="none" stroke="#222" stroke-width="1.2"/><rect x="3.8" y="4.8" width="7.4" height="5.4" fill="none" stroke="#222" stroke-width="1"/><polyline points="3.8,4.8 7.5,8 11.2,4.8" fill="none" stroke="#222" stroke-width="1"/></svg>info@northbeamcaptive.com</div>
    <div class="brand"><span class="brand__dot"></span>NORTHBEAM</div>
  </footer>
</section>

</body>
</html>
```